Roll label Flyer design

I need a flyer for a roll label printer
Pictures for the project are located here:
https://plimtonstickers.sharefile.com/d-k4wq7812m3a0z551

Text I want is located here:
https://plimtonstickers.com/roll-labels.php

Target Market(s)

Manufactures, wholesalers

Industry/Entity Type

Printing

Requirements
Must have
• Lots of pictures. Our phone number 800-472-8164. Website www.plimtonstickers.com

```html
<!DOCTYPE html>
<html lang="en">
<head>
<meta charset="utf-8">
<title>Plimton Stickers – Roll Labels Flyer</title>
<link href="https://fonts.googleapis.com/css2?family=Oswald:wght@500;600&family=Open+Sans:wght@400;600&display=swap" rel="stylesheet">
<style>
  :root{
    --brand-red:#b8141f;
    --ink-gray:#4a4a4c;
    --text-dark:#2a2a2a;
    --stage:#8a8a8a;
    --paper:#ffffff;
    --badge-gray:#6b6b6e;
  }
  *{box-sizing:border-box;margin:0;padding:0}
  html,body{width:1200px;height:1200px;overflow:hidden;background:var(--stage)}
  .flyer{position:absolute;left:171px;top:0;width:857px;height:1200px;background:var(--paper);overflow:hidden;font-family:"Open Sans",Arial,sans-serif;color:var(--text-dark)}
  .backdrop{position:absolute;left:0;top:420px;width:857px;height:700px;background:linear-gradient(180deg,#e6e7ea 0%,#f1f2f3 45%,#fafafa 100%)}
  .art{position:absolute;left:0;top:0}
  .brand{position:absolute;left:258px;top:62px;display:flex;align-items:center;gap:16px}
  .brand-dot{width:62px;height:62px;border-radius:50%;background:var(--brand-red)}
  .brand-name{font-family:"Oswald",Arial,sans-serif;font-weight:500;font-size:30px;letter-spacing:8px;color:var(--paper);text-transform:uppercase}
  .headline{position:absolute;left:30px;top:714px;font-family:"Oswald",Arial,sans-serif;font-weight:600;text-transform:uppercase;line-height:57px;font-size:58px;transform:scaleX(.86);transform-origin:left top}
  .headline .accent{color:var(--brand-red);display:block}
  .headline .main{color:var(--ink-gray);display:block;white-space:nowrap}
  .intro{position:absolute;left:31px;top:841px;width:800px;font-size:15px;line-height:20px;color:var(--text-dark)}
  .tag{position:absolute;display:flex;align-items:center;white-space:nowrap}
  .tag-icon{width:42px;height:42px;border-radius:50%;background:var(--badge-gray);border:3px solid #fff;box-shadow:0 0 0 2px #9a9a9d;position:relative;z-index:2;display:flex;align-items:center;justify-content:center;flex:none}
  .tag-label{margin-left:-10px;padding:3px 18px 3px 22px;background:var(--brand-red);color:#fff;border-radius:0 14px 14px 0;font-family:"Oswald",Arial,sans-serif;font-weight:500;font-size:15px;letter-spacing:-.2px;text-transform:uppercase;white-space:nowrap}
  .tag-features{left:33px;top:906px}
  .tag-features .tag-label{width:132px}
  .tag-markets{left:420px;top:902px}
  .tag-markets .tag-label{width:312px}
  .list{position:absolute;list-style:none;font-size:15px;line-height:20.2px;white-space:nowrap}
  .list li{position:relative;padding-left:16px}
  .list li::before{content:"";position:absolute;left:0;top:7px;width:7px;height:7px;border-radius:50%;background:var(--brand-red)}
  .list-features{left:48px;top:955px}
  .list-markets{left:438px;top:951px}
  .footer{position:absolute;left:0;top:1080px}
  .footer-base{position:absolute;left:0;top:1178px;width:857px;height:22px;background:var(--brand-red)}
  .contact{position:absolute;top:1141px;display:flex;align-items:center;gap:8px;color:#fff;font-size:19px}
  .contact-phone{left:226px}
  .contact-web{left:410px}
</style>
</head>
<body>
<main class="flyer">
  <div class="backdrop" role="img" aria-label="Faint washed-out view of label printing machinery"></div>

  <svg class="art" width="857" height="760" viewBox="0 0 857 760">
    <defs>
      <linearGradient id="heroTone" x1="0" y1="0" x2="1" y2="1">
        <stop offset="0" stop-color="#3a3c55"/>
        <stop offset=".25" stop-color="#5a5fd8" stop-opacity=".85"/>
        <stop offset=".45" stop-color="#cfd0d6"/>
        <stop offset=".7" stop-color="#e9e9ec"/>
        <stop offset="1" stop-color="#2a2b30"/>
      </linearGradient>
      <linearGradient id="rollTone" x1="0" y1="0" x2="1" y2="0">
        <stop offset="0" stop-color="#9a9ea4"/><stop offset=".5" stop-color="#2a2c33"/><stop offset="1" stop-color="#5d6068"/>
      </linearGradient>
      <linearGradient id="pressTone" x1="0" y1="0" x2="1" y2="0">
        <stop offset="0" stop-color="#5c63d6"/><stop offset=".5" stop-color="#dfe1ea"/><stop offset="1" stop-color="#4a50b8"/>
      </linearGradient>
      <linearGradient id="warnTone" x1="0" y1="0" x2="1" y2="1">
        <stop offset="0" stop-color="#3b3b3e"/><stop offset=".5" stop-color="#d3222c"/><stop offset="1" stop-color="#4a4a4d"/>
      </linearGradient>
    </defs>

    <path role="img" aria-label="Close-up photo of printed roll labels running through a press" d="M14 0 H857 V555 C 640 600, 330 470, 60 260 C 28 180, 12 90, 14 0 Z" fill="url(#heroTone)"/>
    <path d="M14 0 C 12 90, 28 180, 60 260 C 330 470, 640 600, 857 555" fill="none" stroke="var(--brand-red)" stroke-width="3"/>

    <line x1="131" y1="345" x2="368" y2="553" stroke="var(--brand-red)" stroke-width="8"/>
    <line x1="368" y1="553" x2="686" y2="607" stroke="var(--brand-red)" stroke-width="8"/>

    <circle cx="131" cy="345" r="123" fill="#fff"/>
    <circle role="img" aria-label="Photo of a wound roll of black printed labels" cx="131" cy="345" r="113" fill="url(#rollTone)"/>
    <circle cx="131" cy="345" r="118" fill="none" stroke="var(--brand-red)" stroke-width="9"/>

    <circle cx="368" cy="553" r="155" fill="#fff"/>
    <circle role="img" aria-label="Photo of label sheets passing a press roller" cx="368" cy="553" r="145" fill="url(#pressTone)"/>
    <circle cx="368" cy="553" r="150" fill="none" stroke="var(--brand-red)" stroke-width="9"/>

    <circle cx="686" cy="607" r="123" fill="#fff"/>
    <circle role="img" aria-label="Photo of red danger warning labels on a roll" cx="686" cy="607" r="113" fill="url(#warnTone)"/>
    <circle cx="686" cy="607" r="118" fill="none" stroke="var(--brand-red)" stroke-width="9"/>
  </svg>

  <div class="brand">
    <span class="brand-dot"></span>
    <span class="brand-name">Plimton Stickers</span>
  </div>

  <h1 class="headline">
    <span class="accent">Outstanding</span>
    <span class="main">Customer Service, Competitive</span>
  </h1>

  <p class="intro">Long or short run. Digital or flexographic. Standard shapes or unique, custom diecuts. Simple spot colors or full color with every embellishment. Let us help you create the perfect label for your application.</p>

  <div class="tag tag-features">
    <span class="tag-icon">
      <svg width="22" height="22" viewBox="0 0 22 22"><rect x="4" y="3" width="13" height="16" rx="1" fill="none" stroke="#fff" stroke-width="1.6"/><path d="M7 8h7M7 11h7M7 14h5" stroke="#fff" stroke-width="1.4"/></svg>
    </span>
    <span class="tag-label">Features:</span>
  </div>
  <ul class="list list-features">
    <li>Foil-Stamping</li>
    <li>Embossing</li>
    <li>Spot Varnishes</li>
    <li>Instant Redeemable Coupons</li>
    <li>Expanded Content/Booklet Labels</li>
  </ul>

  <div class="tag tag-markets">
    <span class="tag-icon">
      <svg width="24" height="24" viewBox="0 0 24 24"><path d="M2 12l5-5 5 3 5-3 5 5-5 5-5-3-5 3z" fill="none" stroke="#fff" stroke-width="1.6" stroke-linejoin="round"/></svg>
    </span>
    <span class="tag-label">Specialty Markets We Service Include:</span>
  </div>
  <ul class="list list-markets">
    <li>Health &amp; Beauty</li>
    <li>Food &amp; Beverage</li>
    <li>Wine &amp; Spirits</li>
    <li>Industrial Safety &amp; Warning</li>
    <li>Promotional</li>
    <li>Compliance (I.E. NSB, QMA, Harlow Rule 42)</li>
  </ul>

  <svg class="footer" width="857" height="120" viewBox="0 0 857 120">
    <path d="M0 102 C 250 -5, 610 -5, 857 102 V120 H0 Z" fill="var(--badge-gray)"/>
    <path d="M0 106 C 250 15, 610 15, 857 106 V120 H0 Z" fill="#fff"/>
    <path d="M0 120 V108 C 250 28, 610 28, 857 108 V120 Z" fill="var(--brand-red)"/>
  </svg>
  <div class="footer-base"></div>

  <div class="contact contact-phone">
    <svg width="14" height="18" viewBox="0 0 14 18"><path d="M4 1 L6 5 L4 7 C5 10 6 12 8 13 L10 11 L13 14 L11 17 C5 16 1 9 2 2 Z" fill="#fff"/></svg>
    <span>(800) 472-8164</span>
  </div>
  <div class="contact contact-web">
    <svg width="18" height="18" viewBox="0 0 18 18"><circle cx="9" cy="9" r="7.5" fill="none" stroke="#fff" stroke-width="1.5"/><path d="M1.5 9h15M9 1.5c-4 4-4 11 0 15M9 1.5c4 4 4 11 0 15" fill="none" stroke="#fff" stroke-width="1.2"/></svg>
    <span>www.plimtonstickers.com</span>
  </div>
</main>
</body>
</html>
```